Design our branded business card!

We'd love for you to design our business card and come up with a fitting design that reflects the Pivex brand. We're a growing tech startup with big ambitions. We've included our brand guidelines (contain colour palette), logo (EPS vector in CMYK) and old designs to help you on your way.

We'd like to keep the design fairly simple:

* Name
* Phone number
* Email address
* Website (www.pivex.life)
* Twitter (@pivex)
* Address (18 Wexham Row, Leeds, UK, LS9 4ZQ).

This would need to include print and cutting marks.

If you have any questions just let us know!

Target Market(s)

Businesses, Press and our customers!

Industry/Entity Type

Business

Contact Information for Business Card

* Name
* Phone number
* Email address
* Twitter (@pivex)

Font styles to use
Sans Serif

Requirements
Must have
• 1. Must have the Pivex logo included.
• 2. Must use the font 'Brandon Text' in either 'light' or 'thin' (https://www.typevault-demo.com/fonts/qrsfonts/halden-sans/)
• 3. Must use exact colours references from the brand guidelines. Colours outside of the brand guidelines will be discounted. White (transparent) backgrounds are fine.
• 4. Must contain the following information:
• * Name
• * Phone number
• * Email address
• * Website (www.pivex.life)
• * Twitter (@pivex)
• * Address (18 Wexham Row, Leeds, UK, LS9 4ZQ).
Nice to have
• Must use the font 'Brandon Text' in either 'light' or 'thin' (https://www.typevault-demo.com/fonts/qrsfonts/halden-sans/)
Should not have
• Colours outside of the brand guidelines will be discounted. White (transparent) backgrounds are fine.
• Avoid creating icons or including photography.

```html
<!DOCTYPE html>
<html lang="en">
<head>
<meta charset="utf-8">
<title>Pivex business card</title>
<link rel="stylesheet" href="https://fonts.googleapis.com/css2?family=Josefin+Sans:wght@300&display=swap">
<style>
  :root {
    --slate: #2b3e3e;
    --slate-lime: #3f6a3c;
    --slate-mist: #4f6361;
    --icon-green: #6fd855;
    --text: #e8eeeb;
  }
  html, body {
    margin: 0;
    padding: 0;
    width: 1200px;
    height: 741px;
    overflow: hidden;
    background: var(--slate);
  }
  .card {
    position: relative;
    width: 1200px;
    height: 741px;
    background: var(--slate);
    overflow: hidden;
  }
  .card__decoration {
    position: absolute;
    inset: 0;
    background: linear-gradient(125deg,
      var(--slate) 0%,
      var(--slate-mist) 30%,
      var(--slate) 48%,
      var(--slate-lime) 62%,
      var(--slate) 80%,
      var(--slate-mist) 100%);
  }
  .contact {
    position: absolute;
    left: 100px;
    top: 53px;
    margin: 0;
    padding: 0;
    list-style: none;
    font-family: "Josefin Sans", sans-serif;
    font-weight: 300;
    font-size: 30px;
    letter-spacing: 0.1em;
    color: var(--text);
  }
  .contact__item {
    display: flex;
    align-items: flex-start;
    line-height: 45px;
    height: 45px;
  }
  .contact__item--address { height: auto; }
  .contact__icon {
    flex: 0 0 36px;
    width: 36px;
    height: 36px;
    margin: 2px 16px 0 0;
    fill: var(--icon-green);
  }
  .contact__text { white-space: nowrap; padding-top: 2px; }
</style>
</head>
<body>
<div class="card">
  <div class="card__decoration" role="img" aria-label="Diagonal decorative bands in lime green and pale grey across the dark card"></div>

  <ul class="contact">
    <li class="contact__item">
      <svg class="contact__icon" viewBox="0 0 24 24" aria-hidden="true"><circle cx="12" cy="6.5" r="4.5"/><path d="M4 23v-5c0-3 2.5-5.5 5.5-5.5h5c3 0 5.5 2.5 5.5 5.5v5z"/></svg>
      <span class="contact__text">Name</span>
    </li>
    <li class="contact__item">
      <svg class="contact__icon" viewBox="0 0 24 24" aria-hidden="true"><path d="M6.6 2.5l3 3.6c.5.6.4 1.4-.1 1.9L8 9.4c1.2 2.6 3.9 5.4 6.6 6.6l1.4-1.5c.5-.5 1.3-.6 1.9-.1l3.6 3c.6.5.7 1.3.2 1.9l-1.7 2.1c-.6.7-1.5 1-2.4.8C10 20.6 3.4 14 1.8 6.4c-.2-.9.1-1.8.8-2.4l2.1-1.7c.6-.5 1.4-.4 1.9.2z"/></svg>
      <span class="contact__text">Phone number</span>
    </li>
    <li class="contact__item">
      <svg class="contact__icon" viewBox="0 0 24 24" aria-hidden="true"><path d="M1 5h22v1.2l-11 7-11-7z"/><path d="M1 8.3l11 7 11-7V19H1z"/></svg>
      <span class="contact__text">Email address</span>
    </li>
    <li class="contact__item">
      <svg class="contact__icon" viewBox="0 0 24 24" aria-hidden="true"><path d="M7 1v19l4-4 3 7 3-1.4-3-6.8h6z"/></svg>
      <span class="contact__text">www.pivex.life</span>
    </li>
    <li class="contact__item">
      <svg class="contact__icon" viewBox="0 0 24 24" aria-hidden="true"><circle cx="12" cy="12" r="9"/></svg>
      <span class="contact__text">@pivex</span>
    </li>
    <li class="contact__item contact__item--address">
      <svg class="contact__icon" viewBox="0 0 24 24" aria-hidden="true"><path d="M12 1a8 8 0 0 0-8 8c0 5.5 8 14 8 14s8-8.5 8-14a8 8 0 0 0-8-8zm0 11a3 3 0 1 1 0-6 3 3 0 0 1 0 6z"/></svg>
      <span class="contact__text">18 Wexham Row, Leeds<br>UK, LS9 4ZQ).</span>
    </li>
  </ul>
</div>
</body>
</html>
```